Business signage half wrap ute

2022 TRX HALBERD UTE BLACK
Looking for a modern, bold half wrap
Brand colours must be incorporated, but with the option to add other colours as we are a uniform printing & signage/wraps business.
Must haves are call to action, phone number 0488 317 965
Website www.kavrinoco.com.au
Services we offer are Uniforms, Signage, Graphic Design
We need something with a big statement on the roads, our target audience are tradesmen
Tradesmen (builders, plumbers, electricians ect
Printing Industry

```html
<!DOCTYPE html>
<html lang="en">
<head>
<meta charset="utf-8">
<title>Kavrino Co – Half Wrap Side Panel</title>
<link href="https://fonts.googleapis.com/css2?family=Montserrat:wght@600;700;800&display=swap" rel="stylesheet">
<style>
  :root {
    --wrap-black: #050505;
    --brand-yellow: #f5c311;
    --brand-white: #f4f4f4;
    --accent-grey: #1c1c1c;
    --backdrop: #ececec;
  }
  html, body {
    margin: 0;
    padding: 0;
    width: 1200px;
    height: 605px;
    overflow: hidden;
    background: var(--backdrop);
    font-family: "Montserrat", Arial, sans-serif;
  }
  .wrap-panel {
    position: absolute;
    left: 50px;
    top: 110px;
    width: 1100px;
    height: 340px;
    background: var(--wrap-black);
    border-radius: 28px;
    overflow: hidden;
  }
  .rear-accent {
    position: absolute;
    right: 40px;
    top: 70px;
    width: 190px;
    height: 190px;
    background: var(--accent-grey);
    transform: rotate(45deg);
  }
  .brand {
    position: absolute;
    left: 250px;
    top: 120px;
    display: flex;
    align-items: center;
    gap: 24px;
  }
  .brand-mark {
    width: 92px;
    height: 92px;
    background: var(--brand-yellow);
  }
  .brand-name {
    margin: 0;
    color: var(--brand-white);
    font-weight: 700;
    font-size: 46px;
    line-height: 1.0;
    letter-spacing: -0.5px;
  }
  .services-band {
    position: absolute;
    left: 0;
    bottom: 40px;
    width: 720px;
    height: 42px;
    background: var(--brand-yellow);
    display: flex;
    align-items: center;
    padding-left: 285px;
    box-sizing: border-box;
  }
  .services-list {
    margin: 0;
    color: var(--wrap-black);
    font-weight: 800;
    font-size: 19px;
    letter-spacing: 0.2px;
    white-space: nowrap;
  }
  .contact {
    position: absolute;
    right: 55px;
    top: 60px;
    text-align: left;
    color: var(--brand-yellow);
  }
  .contact-phone {
    margin: 0;
    font-weight: 800;
    font-size: 28px;
    letter-spacing: 0.5px;
    line-height: 1.1;
  }
  .contact-web {
    margin: 2px 0 0;
    font-weight: 700;
    font-size: 14.5px;
    letter-spacing: 0.2px;
  }
</style>
</head>
<body>
  <section class="wrap-panel" aria-label="Half wrap side panel for TRX HALBERD ute">
    <div class="rear-accent" aria-hidden="true"></div>

    <div class="brand">
      <div class="brand-mark" aria-hidden="true"></div>
      <h1 class="brand-name">KAVRINO<br>CO</h1>
    </div>

    <div class="contact">
      <p class="contact-phone">0488 317 965</p>
      <p class="contact-web">kavrinoco.com.au</p>
    </div>

    <div class="services-band">
      <p class="services-list">UNIFORMS | SIGNAGE | GRAPHIC DESIGN</p>
    </div>
  </section>
</body>
</html>
```